New Menu for Elegant Cafe Pastry Shop

We need to choose a design and layout for our new menu. We would like to also condense our current menu to 4-6 pages.
We will be changing prices and items on the menu, so it needs to be editable. Adobe formats are preferred. The size of the pages needs to be letter size. We will be printing it in house
Please take inspiration from the photos of our shop and food and also our Instagram page.
Attached are our current menu our logo and the logo info

https://www.snapgrid.example/brioweldon/?hl=en
https://maps.example-locate.net/qT7mWx2KpLr9vBn4C

Industry/Entity Type

Food Cafe Bakery pastry

Font styles to use
Other font styles liked:
• please look at attached files

Colors

Designer to choose colors to be used in the design.

Requirements
Nice to have
• Use of Arches like on our shop wallpaper or oblong eclair shapes, Art Deco elements

```html
<!DOCTYPE html>
<html lang="en">
<head>
<meta charset="utf-8">
<title>Brio Weldon – Menu</title>
<link href="https://fonts.googleapis.com/css2?family=Tinos&family=Open+Sans:wght@400;600&display=swap" rel="stylesheet">
<style>
:root{
  --bg:#b9c8c8;
  --page:#ffffff;
  --lav:#dca8f2;
  --lav-line:#c992e4;
  --mint:#64fbc8;
  --mint-line:#4fe0b4;
  --ink:#333333;
  --title-ink:#2a2a2a;
  --gf:#e8424f;
  --cn:#3d7be0;
  --vg:#5ccf3c;
}
html,body{margin:0;padding:0;width:1200px;height:848px;overflow:hidden;background:var(--bg);}
h1,h2,p{font-weight:400;margin:0}
.page{position:absolute;width:567px;height:733px;background:var(--page);transform:scale(.5222);transform-origin:0 0;
  padding:22px 30px;box-sizing:border-box;overflow:hidden;font-family:"Open Sans",sans-serif;font-size:8.4px;color:var(--ink);}
.page-brunch{left:136px;top:34px}
.page-lunch{left:451px;top:34px}
.page-savory{left:766px;top:34px}
.page-sweet{left:303px;top:428px}
.page-drinks{left:618px;top:428px}
.page-title{display:table;margin:0 auto 2px;background:var(--lav);font-family:"Tinos",serif;font-weight:400;font-size:19px;padding:1px 10px;letter-spacing:.4px;color:var(--title-ink);position:relative;z-index:1}
.page-drinks .page-title,.page-drinks .mint-title{background:var(--mint);color:#fff}
.section-title{text-align:center;font-family:"Tinos",serif;font-weight:400;font-size:15px;margin:7px 0 4px;color:var(--title-ink)}
.section-note{text-align:center;font-size:7.5px;margin:-4px 0 6px}
.grid-3{display:grid;grid-template-columns:repeat(3,1fr);column-gap:6px}
.grid-2{display:grid;grid-template-columns:repeat(2,1fr);column-gap:6px}
.bar{display:flex;justify-content:space-between;align-items:center;background:var(--lav);color:#fff;font-family:"Tinos",serif;font-weight:400;font-size:11px;padding:1px 4px;line-height:1.35}
.page-drinks .bar{background:var(--mint)}
.bar .price{font-size:7.5px}
.desc{padding:6px 5px 8px;line-height:1.32;min-height:30px}
.desc.tall{min-height:44px}
.grid-3 .desc{border-right:1px solid var(--lav)}
.grid-3 .desc:nth-child(6n){border-right:0}
.divider{width:340px;height:1px;background:var(--lav-line);margin:4px auto}
.page-drinks .divider{background:var(--mint-line)}
.list-row{display:flex;justify-content:space-between;line-height:1.32}
.tag{display:inline-block;width:8px;height:8px;border-radius:50%;color:#fff;font-size:4px;line-height:8px;text-align:center;vertical-align:middle;font-weight:600}
.tag.gf{background:var(--gf)}.tag.cn{background:var(--cn)}.tag.vg{background:var(--vg)}
.tag.big{width:14px;height:14px;line-height:14px;font-size:8px}
.avail{font-size:5.5px}
.frame-top{position:absolute;top:20px;left:22px;right:22px;height:110px;border:1px solid var(--lav-line);border-bottom:0}
.frame-bottom{position:absolute;left:20px;right:20px;top:600px;bottom:22px;border:1px solid var(--lav-line);border-top:0}
.page-drinks .frame-bottom{border-color:var(--mint-line)}
.fan{position:absolute;width:70px;height:70px;background:radial-gradient(circle at 100% 100%,var(--lav) 0,#ecd2f7 70%,transparent 71%)}
.page-drinks .fan{background:radial-gradient(circle at 100% 100%,var(--mint) 0,#b8fde5 70%,transparent 71%)}
.fan.tl{top:26px;left:28px}
.fan.tr{top:26px;right:28px;transform:scaleX(-1)}
.fan.bl{bottom:30px;left:28px;transform:scaleY(-1)}
.fan.br{bottom:30px;right:28px;transform:scale(-1,-1)}
.brand{text-align:center;margin-top:48px;height:86px;font-family:"Tinos",serif;font-size:22px;letter-spacing:2px;color:#3b3246}
.brand-dot{display:block;width:26px;height:26px;border-radius:50%;background:var(--mint);margin:0 auto 6px}
.sides{background:var(--lav);color:#fff;padding:5px 8px;display:grid;grid-template-columns:1fr 1fr;column-gap:24px;margin-top:4px;font-size:7.8px}
.footnote{text-align:center;font-size:7.5px;margin-top:4px}
.list-grid{display:grid;grid-template-columns:repeat(3,1fr);column-gap:6px}
.list-grid .cell{padding:6px 5px 8px}
.pair{display:grid;column-gap:14px;justify-content:center}
.small-bar{font-size:10px}
.legend{position:absolute;bottom:28px;left:0;right:0;text-align:center;font-size:7.5px}
.legend span{margin:0 10px}
.mint-title{display:table;margin:8px auto 6px;font-family:"Tinos",serif;font-size:13px;padding:1px 12px;width:160px;text-align:center}
.center-list{text-align:center;line-height:1.35}
.split{display:grid;grid-template-columns:1fr 1fr;width:130px;margin:0 auto;text-align:center;line-height:1.3}
.split div:first-child{border-right:1px solid var(--mint-line)}
.tea{display:grid;grid-template-columns:150px 150px;column-gap:8px;justify-content:center}
.tea-col + .tea-col{border-left:1px solid var(--mint-line);padding-left:6px}
.choc{display:grid;grid-template-columns:repeat(3,1fr);column-gap:8px;padding:0 5px}
</style>
</head>
<body>

<section class="page page-brunch">
  <div class="frame-top"></div>
  <div class="fan tl" role="img" aria-label="Lavender fan ornament"></div>
  <div class="fan tr" role="img" aria-label="Lavender fan ornament"></div>
  <div class="brand"><span class="brand-dot"></span>BRIO WELDON</div>
  <h1 class="page-title">ALL DAY BRUNCH</h1>
  <h2 class="section-title">Unique Flavours</h2>
  <div class="grid-3">
    <div class="bar">Grilled Cheese Sandwich <span class="price">$14.00</span></div>
    <div class="bar">Croque Monsieur <span class="price">$15.00</span></div>
    <div class="bar">Croque Madame <span class="price">$16.50</span></div>
    <div class="desc tall">Big chou bun 2 slices of fontina cheese, ham and bacon*– the ultimate grilled cheese sandwich "à la eclair"</div>
    <div class="desc tall">Big chou bun served hot filled with creamy bechamel sauce, gruyère cheese, ham and bacon*</div>
    <div class="desc tall">Big chou bun served hot filled with creamy bechamel sauce, gruyère cheese, ham and bacon* and topped with an egg sunny side up</div>
  </div>
  <div class="divider"></div>
  <h2 class="section-title" style="margin-top:2px">Eggcellent Choices</h2>
  <p class="section-note" style="margin-top:0">Also available: Gluten Free Bun</p>
  <div class="grid-2">
    <div class="bar">Eggs Florentine <span class="price">$16.45</span></div>
    <div class="bar">Avocado &amp; Eggs <span class="price">$17.45</span></div>
    <div class="desc">Chou bun topped with chive cream cheese, sauté spinach, 2 eggs and pink hollandaise sauce</div>
    <div class="desc">Chou bun topped with chunky avocado smash, crumbled feta, 2 eggs, topped with spicy honey, oil, chili flakes and sesame</div>
    <div class="bar">Eggs Benedict <span class="price">$16.45</span></div>
    <div class="bar">Eggs Royal <span class="price">$18.50</span></div>
    <div class="desc">Chou bun topped whipped chive cream cheese, ham, 2 eggs, and pink hollandaise sauce</div>
    <div class="desc">Chou bun, topped with whipped cream cheese with chives, smoked salmon, diced red onion, 2 eggs, pink hollandaise sauce, sesame seeds</div>
  </div>
  <div class="divider"></div>
  <h2 class="section-title" style="margin-top:0">Pancakes</h2>
  <div class="grid-2">
    <div class="bar">O.M.G. Eggs &amp; Bacon <span class="price">$16.50</span></div>
    <div class="bar">Tropical Guava &amp; Cheese <span class="price">$16.00</span></div>
    <div class="desc">4 pancakes topped with grated gruyère, bacon, an egg sunny side up and served with a side of maple syrup</div>
    <div class="desc">4 pancakes topped with guava cream, cream cheese frosting, fresh raspberries and raspberry syrup</div>
    <div class="bar">Classic Noccia &amp; Berries <span class="price">$16.50</span></div>
    <div class="bar">Oriental <span class="price">$14.00</span></div>
    <div class="desc">4 pancakes topped with Noccia, fresh berries and whipped cream</div>
    <div class="desc">4 pancakes topped with Orange cream, caramelized pistachios, crunchy phyllo and drizzled with honey cinnamon syrup <span class="tag cn">CN</span></div>
  </div>
  <h2 class="section-title" style="margin:0">Sides</h2>
  <div class="sides">
    <div>
      <div class="list-row"><span>EGGS(1)</span><span>$2.99</span></div>
      <div class="list-row"><span>BACON (4 SLICES)</span><span>$4.00</span></div>
      <div class="list-row"><span>SALMON</span><span>$3.50</span></div>
      <div class="list-row"><span>PANCAKES (2)</span><span>$3.50</span></div>
    </div>
    <div>
      <div class="list-row"><span>AVOCADO SMASH</span><span>$2.50</span></div>
      <div class="list-row"><span>FRUIT BOWL</span><span>$5.25</span></div>
      <div class="list-row"><span>GREEN SALAD</span><span>$3.50</span></div>
    </div>
  </div>
  <p class="footnote">*Also available Turkey Bacon, Turkey Ham</p>
</section>

<section class="page page-lunch">
  <h1 class="page-title" style="margin-top:6px">LUNCH</h1>
  <h2 class="section-title">Salads</h2>
  <div class="grid-3">
    <div class="bar">Greek <span class="price">$5.50</span></div>
    <div class="bar">Garden Roquefort <span class="price">$5.50</span></div>
    <div class="bar">Zucchini <span class="price">$6.55</span></div>
    <div class="desc tall">Baby tomatoes, cucumbers, feta, olives, onions, P.O.V olive oil, vinegar</div>
    <div class="desc tall">Baby greens, arugula, beets, Roquefort P.O.V blue cheese, caramelized pichachios, strawberries, orange vinaigrette</div>
    <div class="desc tall">Fresh spiralized zucchini with feta, mint, almonds, lemon, P.O.V olive oil</div>
  </div>
  <div class="divider"></div>
  <h2 class="section-title" style="margin-top:0">Soups</h2>
  <div class="grid-3">
    <div class="bar">French Onion Soup <span class="price">$7.95</span></div>
    <div class="bar">Pumpkin Soup <span class="price">$6.60</span></div>
    <div class="bar">Tomato Soup <span class="price">$7.60</span></div>
    <div class="desc tall">Classic onion soup gratinated with gruyere cheese and chunchy eclairs</div>
    <div class="desc tall">Homemade pumpkin soup served with cream and crushed chickpeas</div>
    <div class="desc tall">Tomato soup served with prosciutto gruyere cheese and crunchy eclairs</div>
    <div class="bar">Quiches <span class="price">$6.99</span></div>
    <div class="bar">Phyllo Pocket <span class="price">$4.60</span></div>
    <div class="bar">Brioches <span class="price">$4.30</span></div>
    <div class="desc tall">Available also in GF crust<br>Lorraine<br>Mushroom<br>Spinach<br>Salmon Tomato</div>
    <div class="desc tall">Feta cheese served hot drizzled with honey and seasame</div>
    <div class="desc tall">Ham and cheese<br>Feta and thyme</div>
  </div>
  <div class="divider"></div>
  <h2 class="section-title" style="margin-top:2px">Vegan Treats <span class="tag vg big">V</span></h2>
  <div class="grid-2">
    <div class="bar">Florentine <span class="price">$12.45</span></div>
    <div class="bar">Avocado Toast <span class="price">$15.45</span></div>
    <div class="desc">Chou bun topped with vegan creamy cheese with garlic and herbs, sauté spinach, 2 omelettes</div>
    <div class="desc">Chou bun topped with vegan creamy cheese with garlic and herbs, avocado smash, sliced tomatoes, microgreens and sesame seeds served with a side of spicy honey</div>
  </div>
  <div class="list-grid">
    <div class="bar">Cookies</div><div class="bar">Verrines</div><div class="bar">Muffins</div>
    <div class="cell">
      <div class="list-row"><span>Chocolate chip</span><span>$3.50</span></div>
      <div class="list-row"><span>Double Chocolate Chip</span><span>$3.50</span></div>
      <div class="list-row"><span>Oatmeal Cinnamon</span><span>$3.50</span></div>
      <div class="list-row"><span>Mini Cookies (3 pack)</span><span>$3.10</span></div>
    </div>
    <div class="cell">
      <div class="list-row"><span>Chocolate Cake <span class="tag gf">GF</span></span><span>$6.75</span></div>
      <div class="list-row"><span>Lemon Berries <span class="tag gf">GF</span></span><span>$6.75</span></div>
      <div class="list-row"><span>Coconut Cake <span class="tag gf">GF</span></span><span>$6.75</span></div>
    </div>
    <div class="cell">
      <div class="list-row"><span>Banana Chocolate chip</span><span>$3.00</span></div>
      <div class="list-row"><span>Chocolate/chocolate chips</span><span>$3.00</span></div>
      <div class="list-row"><span>Blueberry</span><span>$3.00</span></div>
      <div class="list-row"><span>Banana Walnut <span class="tag cn">CN</span></span><span>$3.00</span></div>
    </div>
  </div>
  <div class="frame-bottom"></div>
  <div class="fan bl" role="img" aria-label="Lavender fan ornament"></div>
  <div class="fan br" role="img" aria-label="Lavender fan ornament"></div>
  <h2 class="section-title" style="margin:0">Seasonal Treats</h2>
  <p class="section-note" style="margin-top:0">Upon Availability</p>
  <div class="pair" style="grid-template-columns:125px 160px">
    <div>
      <div class="bar small-bar">Travel Cakes <span class="tag vg">V</span></div>
      <div class="cell" style="padding:3px 5px">
        <div class="list-row"><span>Banana pecan <span class="tag cn">CN</span></span><span>$6.00</span></div>
        <div class="list-row"><span>Banana walnut <span class="tag cn">CN</span></span><span>$6.00</span></div>
        <div class="list-row"><span>Banana chocolate chips</span><span>$6.00</span></div>
        <div class="list-row"><span>Blueberry</span><span>$6.00</span></div>
      </div>
      <div class="bar small-bar">Soup</div>
      <div class="list-row" style="padding:3px 5px"><span>Lorraine</span><span>$6.99</span></div>
    </div>
    <div>
      <div class="bar small-bar">Baba Au Rhum <span class="price">Contains Alcohol</span></div>
      <div style="padding:3px 5px">
        <div class="list-row"><span>Chocolate / Noccia</span><span>$7.80</span></div>
        <div class="list-row"><span>Vanilla/orange/pineapple</span><span>$7.80</span></div>
      </div>
      <div class="bar small-bar">Pistachio raspberry opera <span class="price">$8.80</span></div>
      <div style="padding:3px 5px;line-height:1.3">Pistachio joconde cake layered with pistachio buttercream, chocolate ganache and raspberry gelée <span class="tag cn">CN</span></div>
    </div>
  </div>
</section>

<section class="page page-savory">
  <h1 class="page-title" style="margin-top:8px">SAVORY ÉCLAIRS</h1>
  <p class="section-note" style="margin:4px 0 0">Side of green salad | $3.50</p>
  <h2 class="section-title" style="margin-top:2px">Cold</h2>
  <div class="grid-2">
    <div class="bar">Tuna Salad Éclair <span class="price">$7.55</span></div>
    <div class="bar">Roquefort Dream Éclair <span class="price">$9.75</span></div>
    <div class="desc tall">Classic tuna salad with refreshing grapes and celery</div>
    <div class="desc tall">Roquefort cream, Prosciutto, glazed pear wedges, and crushed caramelized pistachios drizzled with Balsamic fig glaze <span class="tag cn">CN</span></div>
    <div class="bar">Caprese Éclair <span class="price">$7.55</span></div>
    <div class="bar">Smoked Salmon Éclair <span class="price">$9.75</span></div>
    <div class="desc">Mozzarella cream, baby tomatoes and mozzarella pearls, topped with fresh basil and balsamic vinegar glaze</div>
    <div class="desc">Whipped cream cheese with chives, smoked salmon, dill, tomatoes and onions</div>
  </div>
  <h2 class="section-title" style="margin-top:0">Hot</h2>
  <div class="grid-2">
    <div class="bar">Shepherd's pie Éclair <span class="price">$9.55</span></div>
    <div class="bar">Mushroom Éclair <span class="price">$9.75</span></div>
    <div class="desc">Seasoned ground beef, topped with creamy mashed potatoes, and grated Parmesan cheese</div>
    <div class="desc">Creamy mashed potatoes, sautéed mushrooms, shaved Parmesan flakes, truffle oil, and chives</div>
    <div class="bar">Chicken, Spinach, Artichoke Éclair <span class="price">$9.75</span></div>
    <div class="bar">Sweet Brie Éclair <span class="price">$9.75</span></div>
    <div class="desc">Rich cream with spinach chicken and artichoke hearts, gratinated with parmesan, gruyere and gouda cheese</div>
    <div class="desc">Melted brie, arugula, strawberry sauce and fresh strawberry halves</div>
  </div>
  <div class="divider"></div>
  <h2 class="section-title" style="margin-top:6px">Petits Gateaux</h2>
  <div class="grid-2">
    <div class="bar">Pumpkin Cheesecake <span class="price">$6.90</span></div>
    <div class="bar">Key Lime Mango <span class="price">$6.90</span></div>
    <div class="desc">New Fall favorite: pumpkin cheesecake served with whipped cream and drizzled with caramel</div>
    <div class="desc">Key lime cream with the sweetness of the mango gelée with a graham cracker insert</div>
    <div class="bar">Chocolate Raspberry Kiss <span class="price">$6.90</span></div>
    <div class="bar">NY Cheesecake Classic <span class="price">$6.90</span></div>
    <div class="desc">Chocolate mousse with a raspberry cremeux center, on a chocolate cookie <span class="tag gf">GF</span></div>
    <div class="desc">Cheesecake made of Brookvale cream cheese on a graham cracker base with a whipped cream rosette</div>
    <div class="bar">Sunset Kiss <span class="price">$8.50</span></div>
    <div class="bar">Napoleon Millefeuille <span class="price">$7.30</span></div>
    <div class="desc tall">Airy passion fruit panna cotta with an insert of almond biscuit and a heart of mango cremeux dipped in yellow mirror glaze and surrounded by a white and yellow chocolate piece sitting on a vanilla cookie <span class="tag cn">CN</span></div>
    <div class="desc tall">Indulge in the exquisite layers of delicate flaky pastry, velvety vanilla pastry cream filling, and airy chantilly that make our Millefeuille – Napoleon a true masterpiece</div>
    <div class="bar">Caramel Strawberry <span class="price">$6.90</span></div>
    <div class="bar">Pavlova <span class="price">$7.50</span></div>
    <div class="desc" style="padding-left:80px">Runny strawberry gelée heart on a meringue cookie enrobed with light golden blond caramel mousse</div>
    <div class="desc" style="padding-right:80px">Pink crispy meringue nest, filled with a light pistachio cream, pieces of fresh strawberries in red fruit gelee and topped with fluffy whipped cream and caramelized pistachios <span class="tag gf">GF</span></div>
  </div>
  <div class="frame-bottom"></div>
  <div class="fan bl" role="img" aria-label="Lavender fan ornament"></div>
  <div class="fan br" role="img" aria-label="Lavender fan ornament"></div>
</section>

<section class="page page-sweet">
  <h1 class="page-title" style="margin-top:6px">SWEET ÉCLAIRS</h1>
  <h2 class="section-title">Single</h2>
  <div class="grid-3">
    <div class="bar">Chocolate Éclair <span class="price">$5.20</span></div>
    <div class="bar">Tres Leches Éclair <span class="price">$5.20</span></div>
    <div class="bar">Strawberry Éclair <span class="price">$5.20</span></div>
    <div class="desc tall">The classic chocolate: pastry filling with chocolate glaze <span class="tag gf">GF</span> <span class="avail">available</span></div>
    <div class="desc tall">Tres leches cream perfumed with real rum and cinnamon, glaze in white chocolate <span class="tag gf">GF</span> <span class="avail">available</span></div>
    <div class="desc tall">Vanilla pastry cream and strawberry jam,dipped in red glaze</div>
    <div class="bar">Vanilla Éclair <span class="price">$5.20</span></div>
    <div class="bar">Coffee Éclair <span class="price">$5.20</span></div>
    <div class="bar">Creme Brulee Éclair <span class="price">$5.20</span></div>
    <div class="desc">The classic: vanilla pastry filling with chocolate glaze <span class="tag gf">GF</span> <span class="avail">available</span></div>
    <div class="desc">Coffee creamy filling with a Caramel Coffee Glaze</div>
    <div class="desc">Filled with classic vanilla pastry cream and dipped in hard caramel</div>
    <div class="bar">Guava Éclair <span class="price">$5.20</span></div><div></div><div></div>
    <div class="desc" style="border-right:0">Guava pastry filling with pink sweet glaze <span class="tag gf">GF</span> <span class="avail">available</span></div><div></div><div></div>
  </div>
  <h2 class="section-title" style="margin-top:-14px">Double</h2>
  <div class="grid-2">
    <div class="bar">German Chocolate Éclair <span class="price">$5.70</span></div>
    <div class="bar">Baklava Éclair <span class="price">$5.70</span></div>
    <div class="desc">Chocolate cream filling topped with a rich sticky coconut and pecan paste dipped in hard dark chocolate with touches of gold <span class="tag cn">CN</span></div>
    <div class="desc">Filled with orange pastry cream, decorated with caramelized pistachios and pieces of fyllo dough drizzled with honey and cinnamon <span class="tag cn">CN</span></div>
    <div class="bar">Tiramisu Éclair <span class="price">$5.70</span></div>
    <div class="bar">Tropical Passion Éclair <span class="price">$5.70</span></div>
    <div class="desc">Double éclair filled with vanilla custard cream flavored with espresso coffee cream and topped with a rich mascarpone cream with an insert of lady fingers cake</div>
    <div class="desc">Double eclair filled with mango pastry cream topped with light passion fruit panna cotta with an insert of mango gelée</div>
  </div>
  <h2 class="section-title" style="margin-top:0">TARTS</h2>
  <div class="grid-3">
    <div class="bar">Key lime Tart <span class="price">$7.95</span></div>
    <div class="bar">La Vie En Rose <span class="price">$8.80</span></div>
    <div class="bar">Fruit Tart <span class="price">$7.95</span></div>
    <div class="desc tall">Classic Key lime tart made of lime Juice from the Keys with meringue rosettes</div>
    <div class="desc tall">Vanilla tart filled with almond frangipane cream and topped with an airy pineapple passionfruit mousse in the shape of a velvety rose</div>
    <div class="desc tall">Sweet vanilla tart filled with Vanilla cream and topped with fresh berries and seasonal fruits</div>
  </div>
  <div class="divider"></div>
  <div class="frame-bottom"></div>
  <div class="fan bl" style="bottom:50px" role="img" aria-label="Lavender fan ornament"></div>
  <div class="fan br" style="bottom:50px" role="img" aria-label="Lavender fan ornament"></div>
  <div class="list-grid" style="margin-top:10px">
    <div class="bar">Bread Puddings <span class="price">$5.20</span></div>
    <div class="bar">Cake Pops <span class="price">$3.50</span></div>
    <div class="bar"><span>Macarons <span class="tag cn">CN</span></span> <span class="price">$3.20</span></div>
    <div class="cell">
      Mango &amp; white Chocolate <span class="tag cn">CN</span><br>Guava <span class="tag cn">CN</span><br>Brownie Walnut <span class="tag cn">CN</span>
      <div class="list-row"><span>Add a scope of Ice cream</span><span>$2.50</span></div>
    </div>
    <div class="cell">
      Vanilla<br>Chocolate<br>Carrot Cake<br>V GF Brownie <span class="tag vg">V</span> <span class="tag gf">GF</span><br><span style="font-size:6.5px">(contains chickpeas)</span>
      <div class="bar" style="margin:6px -5px 6px">Meringues</div>
      <div class="list-row"><span>Meringue box</span><span>$2.50</span></div>
    </div>
    <div class="cell">White Chocolate<br>Dark Chocolate<br>Lemon<br>Apricot<br>Raspberry<br>Pistachio</div>
  </div>
  <div class="legend"><span><span class="tag cn">CN</span> Contains Nuts</span><span><span class="tag gf">GF</span> Gluten Free</span><span><span class="tag vg">V</span> Vegan</span></div>
</section>

<section class="page page-drinks">
  <h1 class="page-title" style="margin-top:6px;width:150px;text-align:center">Mocktails</h1>
  <div class="grid-3" style="margin-top:18px">
    <div class="bar">Pina Colada <span class="price">$6.30</span></div>
    <div class="bar">Mango Lychee <span class="price">$6.50</span></div>
    <div class="bar">Ginger Rosette <span class="price">$6.30</span></div>
    <div class="desc tall">A tropical classic mocktail of pineapple and coconut</div>
    <div class="desc tall">Refreshing mix of lychee and mango</div>
    <div class="desc tall">Ginger ale and grenadine mocktail garnished with maraschino cherry</div>
  </div>
  <div class="divider"></div>
  <h2 class="section-title" style="margin-top:18px">Coffees &amp; Beverages</h2>
  <div class="list-grid">
    <div class="bar">Iced Coffee</div><div class="bar">Hot Coffee</div><div class="bar">Matcha</div>
    <div class="cell">
      <div class="list-row"><span>Iced espresso</span><span>$4.00</span></div>
      <div class="list-row"><span>Iced Cappuccino</span><span>$4.55</span></div>
      <div class="list-row"><span>Iced latte</span><span>$4.75</span></div>
    </div>
    <div class="cell">
      <div class="list-row"><span>Filter Coffee</span><span>$2.40</span></div>
      <div class="list-row"><span>Espresso</span><span>$2.75</span></div>
      <div class="list-row"><span>Cappuccino</span><span>$3.50</span></div>
      <div class="list-row"><span>Latte</span><span>$3.70</span></div>
      <div class="list-row"><span>Americano</span><span>$3.00</span></div>
      <div class="list-row"><span>Espresso Macchiato</span><span>$3.00</span></div>
    </div>
    <div class="cell">
      <div class="list-row"><span>Matcha Tea</span><span>$3.20</span></div>
      <div class="list-row"><span>Matcha Latte hot</span><span>$3.95</span></div>
      <div class="list-row"><span>Matcha latte cold</span><span>$3.95</span></div>
    </div>
  </div>
  <div class="mint-title" style="margin-top:0">Syrups - Sauces - Toppings</div>
  <div class="split"><div>vanilla<br>hazelnut<br>caramel</div><div>mocha<br>lavender<br>almond</div></div>
  <div class="center-list" style="margin-top:6px">(ask for our sugar free options)<br>+$1.00 dark or white chocolate sauce<br>+$1.00 extra shot<br>+$1.00 Decaf</div>
  <div class="mint-title">Tea</div>
  <div class="tea">
    <div class="tea-col">
      <div class="list-row"><span>Earl grey</span><span>$3.50</span></div>
      <div class="list-row"><span>Darjeeling</span><span>$3.50</span></div>
      <div class="list-row"><span>Ginger Lemongrass</span><span>$3.50</span></div>
      <div class="list-row"><span>Camomile</span><span>$3.50</span></div>
    </div>
    <div class="tea-col">
      <div class="list-row"><span>Mint Vervain &amp; Herbs</span><span>$3.50</span></div>
      <div class="list-row"><span>Fruit Symphony</span><span>$3.50</span></div>
      <div class="list-row"><span>Dragon Sencha Green Tea</span><span>$3.50</span></div>
      <div class="list-row"><span>Iced Tea</span><span>$3.50</span></div>
    </div>
  </div>
  <div class="mint-title">Chocolate</div>
  <div class="choc">
    <div class="list-row"><span>Chocolate Hot</span><span>$4.95</span></div>
    <div class="list-row" style="border-left:1px solid var(--mint-line);padding-left:4px"><span>Chocolate Cold</span><span>$4.95</span></div>
    <div class="list-row" style="border-left:1px solid var(--mint-line);padding-left:4px"><span>Whipped Cream</span><span>$1.00</span></div>
  </div>
  <div class="frame-bottom" style="top:615px"></div>
  <div class="fan bl" role="img" aria-label="Mint fan ornament"></div>
  <div class="fan br" role="img" aria-label="Mint fan ornament"></div>
  <div class="mint-title" style="margin-top:28px">Cold Drinks</div>
  <div class="choc">
    <div>
      <div class="list-row"><span>Isla Water 16 oz</span><span>$3.70</span></div>
      <div class="list-row"><span>Fonte Chiara</span><span>$4.70</span></div>
      <div class="list-row"><span>Cola Royale / diet</span><span>$4.00</span></div>
    </div>
    <div style="border-left:1px solid var(--mint-line);padding-left:4px">
      <div class="list-row"><span>Source Vive</span><span>$4.70</span></div>
      <div class="list-row"><span>Homemade Lemonade</span><span>$6.50</span></div>
      <div class="list-row"><span>Mint Lemonade</span><span>$6.50</span></div>
    </div>
    <div style="border-left:1px solid var(--mint-line);padding-left:4px">
      <div class="list-row"><span>Strawberry Lemonade</span><span>$6.50</span></div>
      <div class="list-row"><span>Lavender Lemonade</span><span>$6.50</span></div>
      <div class="list-row"><span>Orange juice</span><span>$4.70</span></div>
    </div>
  </div>
</section>

</body>
</html>
```